Identity Package (Logo, Website)

We need a logo and website design for a new company.
The new company is a voicemail transcription service provider. It's name is KL9BQZ.io
It will be very transactional. We like the "bootstrap" look and feel, and will be using a developer familiar with bootstrap. Here are the kinds of webpages we like :
https://www.lumenvane.io
http://www.quorbil.com/
http://www.plenivo.com/
There will only be 5 pages, as follows :
1- Homepage
2- Voicemail Transcription for Individuals
3- Voicemail Transcription for Companies
4- Wholesale Voicemail Transcription for Service Providers/Enterprises
5- Contact us
As far as the logo is concerned, we'd like to have just stylized text. It should be done in such a way as to make it easy to see the different elements of the name, which are KL, 2, and BQZ.
Reason: I have received a number of designs, but the designs are mostly from the same few designers (not that much variety in designers). I'd like a few more to compare if possible, so I thought I would keep this open until Monday to give more designers the opportunity to submit over the weekend. Thanks!

```html
<!DOCTYPE html>
<html lang="en">
<head>
<meta charset="utf-8">
<title>KL9BQZ — Voicemail Transcription</title>
<link href="https://fonts.googleapis.com/css2?family=Questrial&family=Open+Sans:wght@400;600;700&display=swap" rel="stylesheet">
<style>
:root{
  --brand:#0a8ccf;
  --brand-dark:#0873ab;
  --brand-deep:#06679a;
  --brand-pale:#5fb6e3;
  --orange:#f39c12;
  --ink:#2a2a2a;
  --muted:#666666;
  --line:#e3e3e3;
  --paper:#ffffff;
  --mist:#eeeeee;
}
*{box-sizing:border-box;margin:0;padding:0}
html,body{width:1200px;height:2970px;overflow:hidden}
body{position:relative;background:var(--paper);font-family:"Open Sans",Verdana,sans-serif;color:var(--ink)}

/* header */
.site-header{position:absolute;left:0;top:0;width:1200px;height:145px;background:linear-gradient(#ffffff,#ececec);border-top:10px solid var(--brand)}
.wordmark{position:absolute;font-family:"Questrial",sans-serif;color:var(--brand);letter-spacing:1px;display:flex;align-items:center;gap:10px;white-space:nowrap}
.wordmark .dot{width:14px;height:14px;border-radius:50%;background:currentColor}
.site-header .wordmark{left:63px;top:58px;font-size:38px}
.search{position:absolute;left:931px;top:16px;width:212px;height:31px;border:1px solid #cfcfcf;border-radius:16px;background:#fff;font-size:12px;color:#888;padding:6px 16px;font-family:"Open Sans",sans-serif}
.search svg{position:absolute;right:12px;top:8px}
.main-nav{position:absolute;top:78px;left:434px;display:flex;font-family:"Questrial",sans-serif;font-size:16px;color:#555}
.main-nav a{display:block;flex:0 0 150px;width:150px;text-align:center;color:inherit;text-decoration:none;border-left:1px solid #d4d4d4;line-height:28px;white-space:nowrap}
.main-nav a:first-child{border-left:0;color:var(--brand)}

/* hero */
.hero{position:absolute;left:0;top:145px;width:1200px;height:578px;background:var(--brand);overflow:hidden}
.hero-visual{position:absolute;left:600px;top:90px;width:520px;height:488px;border-radius:50% 50% 0 0;background:radial-gradient(ellipse at 60% 45%,rgba(255,255,255,.30),rgba(255,255,255,.08) 55%,rgba(255,255,255,0) 72%)}
.hero h1{position:absolute;left:103px;top:148px;font-family:"Questrial",sans-serif;font-weight:400;font-size:33px;letter-spacing:3px;color:#fff;white-space:nowrap}
.hero p{position:absolute;left:103px;top:205px;width:500px;font-size:13.5px;line-height:24px;color:#fff}
.btn{position:absolute;display:flex;align-items:center;justify-content:center;gap:6px;font-size:12px;letter-spacing:1px;color:#fff;text-transform:uppercase;white-space:nowrap}
.btn-ghost{left:109px;top:320px;width:150px;height:42px;border:2px solid #fff}
.btn-orange{left:273px;top:320px;width:145px;height:42px;background:var(--orange);border-bottom:3px solid #c97d08}

/* section headings */
.section-title{position:absolute;font-family:"Questrial",sans-serif;font-size:27px;color:var(--brand);display:flex;align-items:center;gap:18px;text-transform:uppercase;white-space:nowrap}
.section-title::after{content:"";position:absolute;left:0;bottom:-10px;width:71px;height:5px;background:#8cc7e8}

/* how it works */
.monitor{position:absolute;left:87px;top:871px;width:446px;height:367px;border-radius:10px;background:linear-gradient(#1d1d1d 0 78%,#d8d8d8 78% 100%);box-shadow:0 14px 18px -12px rgba(0,0,0,.4);z-index:2}
.intro h2{position:absolute;left:626px;top:828px;width:460px;font-size:24px;line-height:27px;font-weight:700;color:var(--brand)}
.intro p{position:absolute;left:626px;width:410px;font-size:14px;line-height:25px;color:var(--muted)}
.btn-solid{left:626px;top:1129px;width:156px;height:39px;background:var(--brand);font-size:12px;letter-spacing:0}

/* steps */
.steps{position:absolute;left:0;top:1204px;width:1200px;height:374px;background:var(--brand)}
.notch{position:absolute;left:578px;top:0;width:0;height:0;border-left:20px solid transparent;border-right:20px solid transparent;border-top:36px solid #fff}
.step{position:absolute;top:132px;width:220px;text-align:center;color:#fff}
.step .ring{width:120px;height:120px;margin:0 auto;border-radius:50%;background:#fff;border:7px solid var(--brand-deep);display:flex;align-items:center;justify-content:center}
.step b{display:block;margin-top:22px;font-size:12px;letter-spacing:1px;font-weight:600}
.step span{display:block;font-size:12px;line-height:16px;margin-top:4px}
.step-arrow{position:absolute;top:138px}

/* about */
.about-photo{position:absolute;left:580px;top:1578px;width:620px;height:422px;background:linear-gradient(90deg,#ffffff 0,#c9c9c9 18%,#8f8f8f 55%,#b4b4b4 100%)}
.about p{position:absolute;left:87px;width:420px;font-size:14px;line-height:25px;color:var(--muted)}

/* pricing */
.pricing{position:absolute;left:0;top:2000px;width:1200px;height:614px;background:var(--mist)}
.plan{position:absolute;background:#fff;box-shadow:0 4px 0 #d5d5d5;text-align:center}
.plan header{height:42px;line-height:42px;background:var(--brand);color:#fff;font-family:"Questrial",sans-serif;font-size:19px}
.plan .price{font-size:30px;font-weight:700;color:var(--ink);height:66px;line-height:66px;margin:0 24px;border-bottom:1px solid var(--line)}
.plan ul{list-style:none;margin:0 24px}
.plan li{font-family:"Questrial",sans-serif;font-size:19px;color:#999;border-bottom:1px solid var(--line)}
.plan .signup{display:block;margin:14px auto 0;width:165px;height:40px;line-height:40px;background:var(--brand);color:#fff;font-family:"Questrial",sans-serif;font-size:20px;border-bottom:3px solid var(--brand-dark)}

/* footer */
.site-footer{position:absolute;left:0;top:2614px;width:1200px;height:356px;background:var(--brand)}
.footer-band{position:absolute;left:0;top:53px;width:1200px;height:49px;background:var(--brand-dark)}
.footer-col{position:absolute;top:66px;color:#fff}
.footer-col h3{font-size:15px;font-weight:600;margin-bottom:15px;letter-spacing:.3px}
.footer-col li{list-style:none;font-size:13px;height:36px;line-height:24px;white-space:nowrap}
.footer-col li::before{content:"-  ";white-space:pre}
.footer-col.social li::before{content:none}
.footer-col.social li{display:flex;align-items:center;gap:8px}
.footer-col.social i{width:24px;height:24px;border-radius:50%;background:#fff;display:inline-block}
.site-footer .wordmark{left:871px;top:229px;font-size:26px;color:#fff}
.copyright{position:absolute;left:0;top:306px;width:1200px;height:50px;line-height:50px;background:var(--brand-deep);color:#fff;font-size:13px;text-align:center}
</style>
</head>
<body>

<header class="site-header">
  <div class="wordmark">KL9BQZ <span class="dot"></span></div>
  <div class="search">Keyword Search
    <svg width="14" height="14" viewBox="0 0 14 14"><circle cx="6" cy="6" r="4.5" fill="none" stroke="#aaa" stroke-width="1.6"/><path d="M9.5 9.5l3.5 3.5" stroke="#aaa" stroke-width="1.8"/></svg>
  </div>
  <nav class="main-nav">
    <a>Home</a><a>Pricing</a><a>Products</a><a>About us</a><a>Contact</a>
  </nav>
</header>

<section class="hero">
  <div class="hero-visual" role="img" aria-label="Hand holding a smartphone showing the app start screen in front of a dotted world map"></div>
  <h1>LOREM IPSUM TEXT SLOGAN</h1>
  <p>Lorem ipsum dolor sit amet, consectetur adipiscing elit. Duis molestie augue eu metus dignissim aliquam semper semper sapien olestie augue. Duis molestie augue eu metus dignissim aliquam augue eu metus dignissim aliquam semper semper.</p>
  <a class="btn btn-ghost">Learn more</a>
  <a class="btn btn-orange">Pricings
    <svg width="13" height="13" viewBox="0 0 13 13"><circle cx="6.5" cy="6.5" r="5.5" fill="none" stroke="#fff" stroke-width="1.4"/><path d="M5 3.8l2.8 2.7L5 9.2" fill="none" stroke="#fff" stroke-width="1.5"/></svg>
  </a>
</section>

<section class="intro">
  <div class="section-title" style="left:87px;top:786px">How it works
    <svg width="40" height="38" viewBox="0 0 40 38"><g fill="none" stroke="#0a8ccf" stroke-width="3" stroke-linejoin="round"><path d="M20 3L37 11 20 19 3 11z"/><path d="M3 18l17 8 17-8"/><path d="M3 25l17 8 17-8"/></g></svg>
  </div>
  <div class="monitor" role="img" aria-label="Desktop monitor playing an introduction video about the service"></div>
  <h2>Lorem ipsum dolor sit amet, consectetur adipiscing elit.</h2>
  <p style="top:898px">Duis molestie augue eu metus dignissim aliquam semper semper sapien. In auctor lobortis erat vel placerat. Nunc tempor eget velit vel blandit.</p>
  <p style="top:1030px">Ut euismod placerat arcu id ullamcorper. Nam venenatis mattis ligula sit amet lacinia semper semper sapien. In auctor lobortis erat vel plac.</p>
  <a class="btn btn-solid">Read more</a>
</section>

<section class="steps">
  <div class="notch"></div>

  <div class="step" style="left:187px">
    <div class="ring"><svg width="56" height="56" viewBox="0 0 56 56"><g fill="none" stroke="#0a8ccf" stroke-width="5"><path d="M10 32V26a18 18 0 0 1 36 0v6"/><path d="M46 34c0 8-6 12-14 12"/></g><rect x="7" y="28" width="10" height="15" rx="3" fill="#0a8ccf"/><rect x="39" y="28" width="10" height="15" rx="3" fill="#0a8ccf"/><rect x="26" y="42" width="8" height="7" rx="2" fill="#0a8ccf"/></svg></div>
    <b>STEP 1.</b><span>Make a voicemail</span>
  </div>
  <div class="step" style="left:391px">
    <div class="ring"><svg width="54" height="54" viewBox="0 0 54 54"><g fill="none" stroke="#0a8ccf" stroke-width="5"><path d="M11 25a16 16 0 0 1 28-9"/><path d="M43 29a16 16 0 0 1-28 9"/></g><path d="M32 10l12 1-3 11z" fill="#0a8ccf"/><path d="M22 44l-12-1 3-11z" fill="#0a8ccf"/></svg></div>
    <b>STEP 2.</b><span>Upload it to KL9BQZ</span>
  </div>
  <div class="step" style="left:593px">
    <div class="ring"><svg width="52" height="52" viewBox="0 0 52 52"><g fill="#0a8ccf" transform="translate(26 26)"><rect x="-5" y="-23" width="10" height="46" rx="2"/><rect x="-5" y="-23" width="10" height="46" rx="2" transform="rotate(45)"/><rect x="-5" y="-23" width="10" height="46" rx="2" transform="rotate(90)"/><rect x="-5" y="-23" width="10" height="46" rx="2" transform="rotate(135)"/><circle r="16"/></g><circle cx="26" cy="26" r="6.5" fill="#fff"/></svg></div>
    <b>STEP 3.</b><span>Wait until processed</span>
  </div>
  <div class="step" style="left:797px">
    <div class="ring"><svg width="52" height="52" viewBox="0 0 52 52"><g fill="none" stroke="#0a8ccf" stroke-width="4" stroke-linejoin="round"><rect x="6" y="22" width="9" height="22"/><path d="M15 24l8-14c2-4 7-2 6 3l-2 8h13c3 0 5 3 4 6l-4 13c-1 2-2 4-5 4H15"/></g></svg></div>
    <b>STEP 4.</b><span>Read the translated<br>Voicemail</span>
  </div>

  <svg class="step-arrow" style="left:362px" width="70" height="28" viewBox="0 0 70 28"><path d="M2 14C22 3 44 3 62 14" fill="none" stroke="#fff" stroke-width="2.4"/><path d="M55 7l9 8-11 3" fill="none" stroke="#fff" stroke-width="2.4"/></svg>
  <svg class="step-arrow" style="left:566px" width="70" height="28" viewBox="0 0 70 28"><path d="M2 14C22 3 44 3 62 14" fill="none" stroke="#fff" stroke-width="2.4"/><path d="M55 7l9 8-11 3" fill="none" stroke="#fff" stroke-width="2.4"/></svg>
  <svg class="step-arrow" style="left:768px" width="70" height="28" viewBox="0 0 70 28"><path d="M2 14C22 3 44 3 62 14" fill="none" stroke="#fff" stroke-width="2.4"/><path d="M55 7l9 8-11 3" fill="none" stroke="#fff" stroke-width="2.4"/></svg>
</section>

<section class="about">
  <div class="about-photo" role="img" aria-label="Black and white photo of colleagues working at laptops in a bright office"></div>
  <div class="section-title" style="left:87px;top:1638px">About KL9BQZ
    <svg width="50" height="32" viewBox="0 0 50 32"><g fill="#0a8ccf"><circle cx="14" cy="8" r="6"/><circle cx="33" cy="7" r="7"/><path d="M2 30c0-9 5-14 12-14s12 5 12 14z"/><path d="M19 30c0-10 6-15 14-15s15 5 15 15z"/></g></svg>
  </div>
  <p style="top:1706px">Lorem ipsum dolor sit amet, consectetur adipiscing elit. Duis molestie augue eu metus dignissim aliquam semper semper sapien. In auctor lobortis erat vel placerat. Nunc tempor eget velit vel blandit.</p>
  <p style="top:1862px">Ut euismod placerat arcu id ullamcorper. Nam venenatis mattis ligula sit amet lacinia semper semper sapien. In auctor lobortis erat vel plac.</p>
</section>

<section class="pricing">
  <div class="section-title" style="left:85px;top:45px">Choose pricing package
    <svg width="34" height="32" viewBox="0 0 34 32"><g fill="none" stroke="#0a8ccf" stroke-width="3" stroke-linejoin="round"><path d="M2 4h6l4 18h16l4-13H10"/></g><circle cx="14" cy="28" r="3" fill="#0a8ccf"/><circle cx="26" cy="28" r="3" fill="#0a8ccf"/></svg>
  </div>

  <article class="plan" style="left:198px;top:190px;width:246px;height:309px">
    <header>PACKAGE NAME</header>
    <div class="price">100$</div>
    <ul><li style="height:47px;line-height:47px">Feature 1</li><li style="height:47px;line-height:47px">Feature 2</li><li style="height:47px;line-height:47px">Feature 3</li></ul>
    <span class="signup">SIGN UP</span>
  </article>

  <article class="plan" style="left:453px;top:146px;width:282px;height:396px">
    <header>PACKAGE NAME</header>
    <div class="price">150$</div>
    <ul><li style="height:45px;line-height:45px">Feature 1</li><li style="height:45px;line-height:45px">Feature 2</li><li style="height:45px;line-height:45px">Feature 3</li><li style="height:40px;line-height:40px">Feature 4</li><li style="height:44px;line-height:44px">Feature 5</li></ul>
    <span class="signup">SIGN UP</span>
  </article>

  <article class="plan" style="left:744px;top:190px;width:246px;height:309px">
    <header>PACKAGE NAME</header>
    <div class="price">120$</div>
    <ul><li style="height:47px;line-height:47px">Feature 1</li><li style="height:47px;line-height:47px">Feature 2</li><li style="height:47px;line-height:47px">Feature 3</li></ul>
    <span class="signup">SIGN UP</span>
  </article>
</section>

<footer class="site-footer">
  <div class="footer-band"></div>
  <div class="footer-col" style="left:184px"><h3>NAVIGATION</h3><ul><li>HOME</li><li>PRICING</li><li>PRODUCTS</li><li>ABOUT US</li><li>CONTACT US</li></ul></div>
  <div class="footer-col" style="left:388px"><h3>SUPPORT</h3><ul><li>DOCUMENTATION</li><li>CUSTOMER SERVICE</li><li>FAQ</li><li>PRODUCT INFORMATION</li></ul></div>
  <div class="footer-col" style="left:649px"><h3>LEGAL</h3><ul><li>TERMS OF SERVICE</li><li>SECURITY</li><li>PRIVACY POLICY</li></ul></div>
  <div class="footer-col social" style="left:863px"><h3>FOLLOW US</h3><ul><li><i></i>- FRIENDLOOP</li><li><i></i>- CHIRPLINE</li><li><i></i>- WORKWEAVE</li></ul></div>
  <div class="wordmark">KL9BQZ <span class="dot" style="width:10px;height:10px"></span></div>
  <div class="copyright">COPYRIGHT © 2014 KL9BQZ ALL RIGHTS RESERVED</div>
</footer>

</body>
</html>
```